Lawn Maintenance Company needs Flyer (Postcard) Design.

Hi everyone.
The majority of what I do is lawn maintenance (grass cutting and trimming/edging).

I'm pretty well open to anything (even humour) but want to stay away from the cartoon/illustration type flyer (but always receptive if you think you have something that might look good, like Pipkin (Thimbles character) :)
Simple but I guess as everyone, something that catches people's eye.

Feel free to kind of play with the name if you think it would help, I would be willing to pay extra if you thought you had a good idea for some type of logo also.

Flyer/Postcard will be front and back, front mainly outlined here, back would be a list of additional services.

Main points I want to get across.
- Professional
- Reliable
- Not like the larger companies that send students or part time
helpers
Kind of want to get those points across without necessarily saying them.

Ok, well, if you haven't rolled your eyes and headed off to the next project.................... :)

Target Market(s)

Mostly regular people with bungalow / two storey houses that don't want to do it themselves and want a nice lawn to frame their house.

Industry/Entity Type

It Company

Requirements
Must have
• Front
** Bramblecrest Landscaping and Lawn Services
** Lawn Maintenance
** (416) 555-3827
** bramblecrestyard@mailvora.com

Back
Commercial and Residential
Plaza Maintenance
Spring/Fall Clean-up
Fertilizing
Weed Prevention
Hedge Trimming
Flower Bed Design
Topdressing
Triplemix
Overseeding
Lawn & flower bed re-edging
Eavestrough Cleaning
Nice to have
• ummmm....grass. lol :)
Birds
Butterflies
Should not have
• Elaborate homes/gardens
Pictures/photos of people

**The pictures I have included are to just give you an idea of the work I do and the type of properties I do**
Please let me know if you want more pics.

```html
<!DOCTYPE html>
<html lang="en">
<head>
<meta charset="utf-8">
<title>Bramblecrest Landscaping and Lawn Services – Postcard</title>
<link rel="stylesheet" href="https://fonts.googleapis.com/css2?family=Marcellus+SC&family=Tinos&family=Arimo&display=swap">
<style>
  :root {
    --lime-center: #dbe51c;
    --lime-mid: #a9d432;
    --lime-edge: #72bd42;
    --forest: #0f6b36;
    --band-green: #0d6d37;
    --headline-yellow: #f5f11f;
    --contact-yellow: #eeea34;
    --silver-light: #f1f3f3;
    --silver-dark: #8a9496;
    --ink: #1b1b1b;
    --page: #efefec;
    --white: #ffffff;
  }
  * { box-sizing: border-box; margin: 0; padding: 0; }
  html, body { width: 1048px; height: 1200px; overflow: hidden; }
  body { background: var(--page); position: relative; }

  .postcard {
    position: absolute;
    left: 124px;
    width: 800px;
    height: 560px;
    overflow: hidden;
    box-shadow: 0 4px 14px rgba(0,0,0,.18);
  }
  .postcard--front {
    top: 30px;
    background: radial-gradient(ellipse 70% 75% at 52% 42%, var(--lime-center) 0%, var(--lime-mid) 50%, var(--lime-edge) 100%);
  }
  .postcard--back { top: 610px; background: var(--white); }

  .back-panel {
    position: absolute; left: 0; top: 0; width: 403px; height: 560px;
    background: radial-gradient(ellipse 80% 70% at 88% 48%, var(--lime-center) 0%, var(--lime-mid) 50%, var(--lime-edge) 100%);
  }

  .ground { position: absolute; left: 0; top: 0; width: 800px; height: 560px; }

  .service-tag {
    position: absolute; top: 34px; left: 0; width: 100%;
    text-align: center;
    font-family: "Tinos", serif; font-size: 52px;
    color: var(--headline-yellow);
    text-shadow: 0 0 4px #3f6a12, 0 0 8px rgba(40,80,10,.6);
  }
  .company-name {
    position: absolute; top: 140px; left: 0; width: 100%;
    text-align: center;
    font-family: "Marcellus SC", serif; font-size: 60px; line-height: 72px;
    color: var(--forest);
  }

  .contact {
    position: absolute; right: 31px; text-align: right;
    font-family: "Arimo", sans-serif; color: var(--contact-yellow);
  }
  .contact--phone { top: 468px; font-size: 31px; }
  .contact--email { top: 509px; font-size: 25px; }
  .contact--call-us { top: 496px; font-size: 31px; }

  .butterfly { position: absolute; border-radius: 50%; }
  .butterfly--green {
    background: radial-gradient(circle, #e9f05a 0%, #8cc63e 55%, rgba(60,140,40,0) 72%);
  }
  .butterfly--silver {
    background: radial-gradient(circle, #ffffff 0%, #9ea6a8 55%, rgba(120,130,130,0) 72%);
  }

  .services-title {
    position: absolute; left: 33px; top: 48px;
    font-family: "Marcellus SC", serif; font-size: 29px; color: var(--forest);
  }
  .services-list {
    position: absolute; left: 33px; top: 94px; list-style: none;
    font-family: "Marcellus SC", serif; font-size: 17px; line-height: 25.3px; color: var(--forest);
  }
  .services-list li { display: flex; align-items: center; }
  .services-list li::before {
    content: ""; width: 8px; height: 8px; margin-right: 10px; border-radius: 50%;
    background: #dfe6d4; border: 1.5px solid #6c7d6a;
  }

  .return-address {
    position: absolute; left: 416px; top: 16px;
    font-family: "Arimo", sans-serif; font-size: 14px; line-height: 17px; color: var(--ink);
  }
  .return-address p + p { margin-top: 3px; }

  .indicia {
    position: absolute; left: 692px; top: 12px; width: 87px; height: 98px;
    border: 1.5px solid var(--ink);
    display: flex; flex-direction: column; justify-content: center; align-items: center;
    font-family: "Arimo", sans-serif; font-size: 10.5px; line-height: 13px; color: var(--ink); text-align: center;
  }
  .indicia .paid { font-size: 15px; line-height: 17px; }

  .addressee {
    position: absolute; left: 607px; top: 122px; width: 172px; height: 85px;
    border: 1.5px solid var(--ink);
    padding: 25px 0 0 20px;
    font-family: "Arimo", sans-serif; font-size: 15px; line-height: 19px; color: var(--ink);
  }
</style>
</head>
<body>

<section class="postcard postcard--front" aria-label="Postcard front">
  <svg class="ground" viewBox="0 0 800 560" aria-hidden="true">
    <defs>
      <linearGradient id="frontSilver" x1="0" x2="1" y1="0" y2="0">
        <stop offset="0" stop-color="var(--silver-dark)"/>
        <stop offset=".45" stop-color="var(--silver-light)"/>
        <stop offset="1" stop-color="var(--silver-dark)"/>
      </linearGradient>
      <linearGradient id="frontGrass" x1="0" x2="0" y1="0" y2="1">
        <stop offset="0" stop-color="#9fd34a" stop-opacity="0"/>
        <stop offset=".45" stop-color="#4fa634"/>
        <stop offset="1" stop-color="#1f7a2c"/>
      </linearGradient>
    </defs>
    <path d="M0 455 C 160 505, 360 505, 540 445 S 740 380, 800 395 L800 560 L0 560 Z" fill="var(--band-green)"/>
  </svg>
  <svg class="ground" viewBox="0 0 800 560" role="img" aria-label="Illustrated strip of fresh green grass blades along the lower edge">
    <path d="M0 380 L 560 380 C 420 470, 200 500, 0 470 Z" fill="url(#frontGrass)"/>
  </svg>
  <svg class="ground" viewBox="0 0 800 560" aria-hidden="true">
    <path d="M0 440 C 160 500, 360 505, 540 440 S 740 372, 800 382 L800 395 C 740 380, 640 400, 540 445 C 360 505, 160 505, 0 455 Z" fill="url(#frontSilver)"/>
  </svg>

  <div class="butterfly butterfly--green" style="left:700px; top:270px; width:92px; height:82px;" role="img" aria-label="Green butterfly illustration"></div>
  <div class="butterfly butterfly--silver" style="left:700px; top:362px; width:60px; height:54px;" role="img" aria-label="Silver butterfly illustration"></div>

  <h2 class="service-tag">Lawn Maintenance</h2>
  <h1 class="company-name">Bramblecrest<br>Landscaping and<br>Lawn Services</h1>

  <p class="contact contact--phone">Call: (416) 555-3827</p>
  <p class="contact contact--email">bramblecrestyard@mailvora.com</p>
</section>

<section class="postcard postcard--back" aria-label="Postcard back">
  <div class="back-panel"></div>

  <svg class="ground" viewBox="0 0 800 560" aria-hidden="true">
    <defs>
      <linearGradient id="backSilver" x1="0" x2="1" y1="0" y2="0">
        <stop offset="0" stop-color="var(--silver-dark)"/>
        <stop offset=".45" stop-color="var(--silver-light)"/>
        <stop offset="1" stop-color="var(--silver-dark)"/>
      </linearGradient>
      <linearGradient id="backGrass" x1="0" x2="0" y1="0" y2="1">
        <stop offset="0" stop-color="#9fd34a" stop-opacity="0"/>
        <stop offset=".45" stop-color="#4fa634"/>
        <stop offset="1" stop-color="#1f7a2c"/>
      </linearGradient>
    </defs>
    <path d="M0 455 C 160 505, 360 505, 540 445 S 740 380, 800 395 L800 560 L0 560 Z" fill="var(--band-green)"/>
  </svg>
  <svg class="ground" viewBox="0 0 800 560" role="img" aria-label="Illustrated strip of fresh green grass blades running across the card">
    <path d="M0 400 L 780 400 C 700 420, 620 420, 540 440 C 360 500, 160 500, 0 470 Z" fill="url(#backGrass)"/>
  </svg>
  <svg class="ground" viewBox="0 0 800 560" aria-hidden="true">
    <path d="M0 440 C 160 500, 360 505, 540 440 S 740 372, 800 382 L800 395 C 740 380, 640 400, 540 445 C 360 505, 160 505, 0 455 Z" fill="url(#backSilver)"/>
  </svg>

  <div class="butterfly butterfly--green" style="left:692px; top:318px; width:96px; height:84px;" role="img" aria-label="Green butterfly illustration"></div>
  <div class="butterfly butterfly--silver" style="left:706px; top:410px; width:60px; height:54px;" role="img" aria-label="Silver butterfly illustration"></div>

  <h2 class="services-title">Services</h2>
  <ul class="services-list">
    <li>Commercial and Residential</li>
    <li>Plaza Maintenance</li>
    <li>Spring/Fall Clean-up</li>
    <li>Fertilizing</li>
    <li>Weed Prevention</li>
    <li>Hedge Trimming</li>
    <li>Flower Bed Design</li>
    <li>Topdressing</li>
    <li>Triplemix</li>
    <li>Overseeding</li>
    <li>Lawn &amp; flower bed re-edging</li>
    <li>Eavestrough Cleaning</li>
  </ul>

  <div class="return-address">
    <p>Return Address</p>
    <p>Bramblecrest Landscaping and<br>Lawn Services</p>
    <p>Street Name, City Name<br>State, ZipCode</p>
  </div>

  <div class="indicia">
    <span>PRSRT STD</span>
    <span>ECRWSS</span>
    <span>U.S.POSTAGE</span>
    <span class="paid">PAID</span>
    <span>EDDM Retail</span>
  </div>

  <div class="addressee">Local<br>Postal Customer</div>

  <p class="contact contact--call-us">Call Us (416) 555-3827</p>
</section>

</body>
</html>
```